Tree Service Billboard 20x8 ft

We need a billboard design for a tree service company.
The billboard is 20ft x 8 ft so we need a design that is capable to stretching to those dimensions without loosing quality.
I have attached a series of images.
Image 1- Simply a billboard that I think looks good that I would like you to use for inspiration. I am aiming for the same format only no color in the wording, just black white, or gray. I like the the trees in the background, the logo placed to the left, and wording on the right.
Image 2- Current Logo I would like to the left of the billboard
Image 3- Another format of current logo if needed.
Image 4- A drawn out design template
Image 5- Another drawn out design template

Specific things I am looking for
-The contact number to be the largest thing on the design
-The logo on the design
-Key points to the design to say:
Tree Removal
Tree Trimming
Land Development
Stump Grinding
Storm Response
Insured
Free Bids
-The facebook logo
-The Google Logo

```html
<!DOCTYPE html>
<html lang="en">
<head>
<meta charset="utf-8">
<title>Elmwood Arborists – Billboard</title>
<link rel="stylesheet" href="https://fonts.googleapis.com/css2?family=Poppins:wght@700&family=Lilita+One&display=swap">
<style>
  :root {
    --backdrop: #8a8a8a;
    --canopy-deep: #0c1a0c;
    --canopy-mid: #1f3a1d;
    --canopy-light: #3b5a36;
    --band-light: #8dc63f;
    --band-shadow: #3f7a33;
    --ink: #141414;
    --white: #ffffff;
  }
  html, body {
    margin: 0;
    width: 1200px;
    height: 1200px;
    overflow: hidden;
    background: var(--backdrop);
  }
  .billboard {
    position: absolute;
    left: 62px;
    top: 385px;
    width: 1075px;
    height: 430px;
    display: block;
  }
  .brand-name { font-family: "Poppins", sans-serif; font-weight: 700; fill: var(--white); }
  .main-phone { font-family: "Poppins", sans-serif; font-weight: 700; fill: var(--white); }
  .service-label { font-family: "Lilita One", sans-serif; fill: var(--ink); }
  .band-light { fill: var(--band-light); }
  .band-shadow { fill: var(--band-shadow); }
  .ring { fill: none; stroke: var(--white); }
</style>
</head>
<body>
<svg class="billboard" viewBox="0 0 860 344" xmlns="http://www.w3.org/2000/svg">
  <defs>
    <radialGradient id="canopyGlow" cx="0.5" cy="0.45" r="0.7">
      <stop offset="0" stop-color="var(--canopy-light)"/>
      <stop offset="0.45" stop-color="var(--canopy-mid)"/>
      <stop offset="1" stop-color="var(--canopy-deep)"/>
    </radialGradient>
  </defs>

  <rect class="canopy-photo" role="img" aria-label="Photo looking up through a green tree canopy with sunlight breaking through the branches" x="0" y="0" width="860" height="344" fill="url(#canopyGlow)"/>

  <g class="brand">
    <circle class="ring" cx="62" cy="118" r="14" stroke-width="2.5"/>
    <text class="brand-name" x="86" y="126" font-size="20">Elmwood Arborists</text>
  </g>

  <text class="main-phone" x="48" y="296" font-size="29">555-014-2290</text>

  <g class="social-links">
    <circle class="ring" cx="365" cy="290" r="17" stroke-width="2.5"/>
    <circle class="ring" cx="417" cy="290" r="17" stroke-width="2.5"/>
  </g>

  <g class="service-list">
    <polygon class="band-shadow" points="475,37 860,37 860,70 477,70"/>
    <polygon class="band-light" points="490,37 860,37 860,70 492,70"/>
    <text class="service-label" x="578" y="61" font-size="22">Tree Removal</text>

    <polygon class="band-shadow" points="478,77 860,77 860,110 480,110"/>
    <polygon class="band-light" points="493,77 860,77 860,110 495,110"/>
    <text class="service-label" x="578" y="101" font-size="22">Tree Trimming</text>

    <polygon class="band-shadow" points="481,117 860,117 860,150 483,150"/>
    <polygon class="band-light" points="496,117 860,117 860,150 498,150"/>
    <text class="service-label" x="578" y="141" font-size="22">Land Development</text>

    <polygon class="band-shadow" points="484,157 860,157 860,190 486,190"/>
    <polygon class="band-light" points="499,157 860,157 860,190 501,190"/>
    <text class="service-label" x="578" y="181" font-size="22">Stump Grinding</text>

    <polygon class="band-shadow" points="487,197 860,197 860,230 489,230"/>
    <polygon class="band-light" points="502,197 860,197 860,230 504,230"/>
    <text class="service-label" x="578" y="221" font-size="22">Storm Response</text>

    <polygon class="band-shadow" points="490,237 860,237 860,270 492,270"/>
    <polygon class="band-light" points="505,237 860,237 860,270 507,270"/>
    <text class="service-label" x="578" y="261" font-size="22">Insured</text>

    <polygon class="band-shadow" points="493,277 860,277 860,310 495,310"/>
    <polygon class="band-light" points="508,277 860,277 860,310 510,310"/>
    <text class="service-label" x="578" y="301" font-size="22">Free Bids</text>
  </g>
</svg>
</body>
</html>
```